Business card for denture clinic Plendora

We need a new business card with our new logo. We are a denture clinic in New Zealand with our target market being 45+ years old. We would need a space on the back to write our patients next appointment on. We would space for only one appointment rather than a list. We will attach a photo showing an example of this. But of course, we would like to see your twist on this. We want it to be bold and easy to read and a good mixture of professional but modern. We have attached our logo to be used on the card.

Target Market(s)

People aged 45+ needing dentures

Industry/Entity Type

Dental

Contact Information for Business Card

We want our logo on the front and the space to write an appointment on the back. I've attached an example our our old business card showing this. We need to have the technicians details on the front.

Font styles to use
Sans Serif

Colors
0255a3
919191
fbfbfb

Requirements
Must have
• The following details:
• Ray Dunmore BDT, PGDipCDentTech Kerrow
• Dental Prosthetist
• Phone numbers: 0800 47 3215
• 09 517 2943
• Email: ray@plendora.co.nz
• www.plendora.co.nz
• Address: 148 Mirelle Road
• Te Atatu South
• Auckland 0745
Nice to have
• We would like our business cards to have more than just two colours as we want them to be more vibrant. We have uploaded an example of a business card we liked that showed this.

```html
<!DOCTYPE html>
<html lang="en">
<head>
<meta charset="utf-8">
<title>Plendora – Business Card</title>
<link href="https://fonts.googleapis.com/css2?family=Open+Sans:wght@400;600;700&display=swap" rel="stylesheet">
<style>
  :root{
    --bg:#2b3036;
    --paper:#fbfbfb;
    --blue:#0255a3;
    --grey:#919191;
    --teal:#67e3de;
    --yellow:#fbbd3a;
    --ink:#123a6b;
  }
  *{box-sizing:border-box;margin:0;padding:0}
  html,body{width:1200px;height:938px;overflow:hidden}
  body{background:var(--bg);font-family:"Open Sans",Arial,sans-serif;position:relative}
  .card{position:absolute;top:164px;width:340px;height:610px;background:var(--paper);overflow:hidden;box-shadow:0 8px 24px rgba(0,0,0,.35)}
  .card--front{left:190px}
  .card--back{left:670px}

  .hairline{position:absolute;width:1px;background:#c9c9c9}
  .accent-bar{position:absolute;width:6px;background:var(--blue)}

  /* front */
  .name-panel{position:absolute;left:120px;top:34px;width:220px;height:240px;background:var(--teal);border-radius:44px 0 0 44px;padding:34px 18px 0 26px;color:var(--ink)}
  .role{font-size:12px;font-weight:600}
  .tech-name{font-size:31px;font-weight:700;color:var(--blue);line-height:1.1;margin:4px 0 6px}
  .quals{font-size:11.5px;font-weight:600}

  .brand{position:absolute;left:34px;width:272px;display:flex;align-items:center;gap:12px}
  .card--front .brand{top:300px}
  .card--back .brand{top:250px}
  .brand-square{width:40px;height:40px;background:var(--blue);flex:none}
  .brand-name{font-size:33px;font-weight:600;letter-spacing:2px;color:var(--blue);line-height:1}
  .brand-tag{font-size:11px;letter-spacing:3.2px;color:var(--grey);margin-top:6px}

  .contact-panel{position:absolute;left:0;top:396px;width:270px;height:184px;background:var(--yellow);border-radius:0 48px 48px 0;padding:26px 18px 0 22px;color:var(--ink)}
  .phone{font-size:19px;font-weight:700;line-height:1.3}
  .line{font-size:12px;font-weight:600;line-height:1.55}
  .phones{margin-bottom:8px}
  .address{margin-top:8px}

  /* back */
  .back-shape{position:absolute;inset:0}
  .appointment{position:absolute;left:32px;top:398px;width:238px;height:150px;background:var(--paper);border-radius:34px;padding:34px 24px 0 26px;color:var(--blue)}
  .appt-row{display:flex;align-items:flex-end;font-size:13px;font-weight:600;margin-bottom:24px}
  .appt-row span{flex:1;border-bottom:2px dotted var(--blue);margin-left:4px;height:12px}
</style>
</head>
<body>

<section class="card card--front" aria-label="Front of business card">
  <div class="hairline" style="left:84px;top:0;height:150px"></div>
  <div class="hairline" style="left:300px;top:500px;height:110px"></div>
  <div class="name-panel">
    <p class="role">Dental Prosthetist</p>
    <p class="tech-name">Ray Dunmore</p>
    <p class="quals">BDT, PGDipCDentTech Kerrow</p>
  </div>
  <div class="accent-bar" style="right:8px;top:270px;height:150px"></div>
  <div class="brand">
    <div class="brand-square"></div>
    <div>
      <p class="brand-name">PLENDORA</p>
      <p class="brand-tag">THE DENTURE EXPERTS</p>
    </div>
  </div>
  <div class="accent-bar" style="left:8px;top:390px;height:150px;display:none"></div>
  <div class="accent-bar" style="left:8px;top:14px;height:160px"></div>
  <div class="contact-panel">
    <div class="phones">
      <p class="phone">0800 47 3215</p>
      <p class="phone">09 517 2943</p>
    </div>
    <p class="line">ray@plendora.co.nz</p>
    <p class="line">www.plendora.co.nz</p>
    <p class="line address">148 Mirelle Road, Te Atatu South</p>
    <p class="line">Auckland 0745</p>
  </div>
</section>

<section class="card card--back" aria-label="Back of business card">
  <svg class="back-shape" width="340" height="610" viewBox="0 0 340 610" aria-hidden="true">
    <path d="M340 0 H170 C220 70 270 130 300 200 C310 225 326 240 340 240 Z" fill="var(--yellow)"/>
    <path d="M0 360 C120 340 230 320 330 350 V610 H0 Z" fill="var(--teal)"/>
    <line x1="50" y1="0" x2="50" y2="120" stroke="#c9c9c9" stroke-width="1"/>
  </svg>
  <div class="accent-bar" style="left:10px;top:360px;height:150px"></div>
  <div class="accent-bar" style="right:10px;top:240px;height:160px"></div>
  <div class="brand">
    <div class="brand-square"></div>
    <div>
      <p class="brand-name">PLENDORA</p>
      <p class="brand-tag">THE DENTURE EXPERTS</p>
    </div>
  </div>
  <div class="appointment">
    <p class="appt-row">Date<span></span></p>
    <p class="appt-row">Time<span></span></p>
  </div>
</section>

</body>
</html>
```